Sparkling Wine Label Wren Hollow

Super Premium Sparkling Wine Label

We are a super premium tasmanian fine wine producer and are about to release our first Sparking Wine.

please visit www.wrenhollowvines.com.au to check out our range of wine. We need a label that will sit within this branding but as the aspirational product. We think that the Mavet grey/navy label will fit into this concept. It is masculine clean elegent and very smick,
and would be a great addition to our line see Copper Pinot Noir label.

However you can be quite creative with Sparkling Line eg Tollis Prime Reserve is a stunning classical french label featuring gold baroque detail and feminine elegence.

Its up to you if you where spending $50 on a special bottles of sparkling wine what would you expect to see?

Black/Gold Graphite/Gold

Needs a neck /collar label

Main Front Label
Wren Hollow
Chardonnay Pinot Noir
Tasmania

Back label has all the techical into you can use the back label from existing labels but reverserve out the colours to black and white or graphite and white

We want a label that oozes quality and expense. That says this the way I want to celebrate.

Target Market(s)

40 60 age group appreciator of quality

Industry/Entity Type

Product

Requirements
Must have
• Neck label
Simular to Mavet Shield so
WREN arched above
G rondel in middle possibiliy replacing coat of arms
TASMANIA arched under in red

Main Front Label
Wren Hollow
Tasmania
Chardonnay Pinot Noir 750ML

Back Label / use the attachment Wren label just reverse out so that it is a black label with white writing and amend information
Wren Hollow
23 Ferny Marsh Rd Dunleigh
Tasmania, 7190
0417293856
www.wrenhollowvines.com.au
contact@wrenhollowvines.com.au
Sulphur Dioxide Added
Alc/Vol 12.5%
7.7 Standard Drinks

Rondel g
Nice to have

```html
<!DOCTYPE html>
<html lang="en">
<head>
<meta charset="utf-8">
<title>Wren Hollow – Chardonnay Pinot Noir Labels</title>
<link rel="stylesheet" href="https://fonts.googleapis.com/css2?family=Pinyon+Script&family=Arimo&family=Libre+Caslon+Text&family=Open+Sans&family=Cinzel:wght@700&display=swap">
<style>
  :root {
    --backdrop: #3b2a20;
    --ink: #111008;
    --gold-light: #f6e79a;
    --gold-mid: #e2c65a;
    --gold-deep: #c4a033;
    --map-cream: #f3ead0;
    --seal-red: #c0282c;
    --seal-cream: #f2ecd8;
  }
  * { margin: 0; padding: 0; box-sizing: border-box; }
  html, body { width: 1200px; height: 1200px; overflow: hidden; background: var(--backdrop); }
  .canvas { position: relative; width: 1200px; height: 1200px; }

  .label {
    position: absolute;
    background: linear-gradient(100deg, var(--gold-deep) 0%, var(--gold-mid) 30%, var(--gold-light) 55%, var(--gold-mid) 80%, var(--gold-deep) 100%);
    border: 6px solid var(--ink);
  }
  .label::before {
    content: ""; position: absolute; inset: 8px;
    border: 4px solid var(--ink);
  }

  /* Front label */
  .front { left: 48px; top: 40px; width: 592px; height: 508px; }
  .front__name {
    position: absolute; left: 40px; top: 20px; width: 500px; text-align: center;
    font: 230px/1 "Pinyon Script", cursive; color: var(--ink);
  }
  .front__sub {
    position: absolute; left: 0; width: 100%; top: 286px; text-align: center;
    font: 40px/1 "Arimo", sans-serif; color: var(--ink); letter-spacing: 1px; padding-left: 40px;
  }
  .front__variety {
    position: absolute; left: 0; width: 100%; top: 370px; text-align: center;
    font: 50px/1 "Pinyon Script", cursive; color: var(--ink);
  }
  .front__volume, .front__region {
    position: absolute; top: 442px; font: 32px/1 "Libre Caslon Text", serif; color: var(--ink);
  }
  .front__volume { left: 46px; }
  .front__region { right: 46px; }

  /* Back label */
  .back { left: 72px; top: 612px; width: 546px; height: 546px; }
  .back__map {
    position: absolute; left: 330px; top: 36px; width: 180px; height: 450px;
    background: radial-gradient(closest-side at 50% 45%, var(--map-cream) 0%, rgba(243,234,208,.6) 55%, rgba(243,234,208,0) 100%);
  }
  .back__details {
    position: absolute; left: 36px; top: 36px; z-index: 1;
    font: 16px/22.5px "Open Sans", sans-serif; color: var(--ink); list-style: none;
  }
  .back__seal { position: absolute; left: 34px; top: 306px; width: 164px; height: 164px; }
  .back__footer {
    position: absolute; left: 36px; bottom: 24px;
    font: 25px/1 "Libre Caslon Text", serif; color: var(--ink);
  }

  /* Neck label */
  .neck { position: absolute; left: 668px; top: 36px; width: 490px; height: 1140px; }
  .neck__name {
    position: absolute; left: 245px; top: 440px; transform: translate(-50%,-50%) rotate(90deg);
    font: 170px/1 "Pinyon Script", cursive; color: var(--ink); white-space: nowrap;
  }
  .neck__seal-name {
    position: absolute; left: 0; width: 100%; top: 858px; text-align: center;
    font: 700 42px/1 "Cinzel", serif; color: var(--ink); letter-spacing: 4px;
  }
  .neck__region {
    position: absolute; left: 0; width: 100%; top: 1060px; text-align: center;
    font: 700 22px/1 "Cinzel", serif; color: var(--seal-red); letter-spacing: 3px;
  }
</style>
</head>
<body>
<main class="canvas">

  <section class="label front" aria-label="Front label">
    <div class="front__name">Wren</div>
    <div class="front__sub">HOLLOW</div>
    <div class="front__variety">Chardonnay Pinot Noir</div>
    <div class="front__volume">750ml</div>
    <div class="front__region">Tasmania</div>
  </section>

  <section class="label back" aria-label="Back label">
    <div class="back__map" role="img" aria-label="Map of the East Coast region of Tasmania showing the vineyard location"></div>
    <ul class="back__details">
      <li>Wren Hollow</li>
      <li>23 Ferny Marsh Road Dunleigh</li>
      <li>Tasmania Australia 7190</li>
      <li>0417 293 856</li>
      <li>contact@wrenhollowvines.com.au</li>
      <li>www.wrenhollowvines.com.au</li>
      <li>Alc/Vol 12.5 Standard drinks 8</li>
      <li>Sulphur Dioxide added</li>
      <li>7.7 Standard Drinks</li>
    </ul>
    <svg class="back__seal" viewBox="0 0 170 170" aria-label="Wren Hollow seal">
      <circle cx="85" cy="85" r="80" fill="var(--seal-cream)" stroke="#999" stroke-width="1.5"/>
      <text x="85" y="92" text-anchor="middle" font-family="Open Sans, sans-serif" font-size="20" fill="#111008">Wren Hollow</text>
    </svg>
    <div class="back__footer">Wine of Australia</div>
  </section>

  <section class="neck" aria-label="Neck label">
    <svg width="490" height="1140" viewBox="0 0 490 1140" style="position:absolute;left:0;top:0">
      <defs>
        <linearGradient id="neckGold" x1="0" x2="1" y1="0" y2="0">
          <stop offset="0" stop-color="var(--gold-deep)"/>
          <stop offset=".35" stop-color="var(--gold-mid)"/>
          <stop offset=".6" stop-color="var(--gold-light)"/>
          <stop offset="1" stop-color="var(--gold-deep)"/>
        </linearGradient>
      </defs>
      <path d="M0 0 H490 V1020 H400 L370 1050 Q370 1100 245 1140 Q120 1100 120 1050 L90 1020 H0 Z" fill="url(#neckGold)"/>
      <rect x="0" y="128" width="490" height="6" fill="var(--ink)"/>
      <rect x="0" y="846" width="150" height="6" fill="var(--ink)"/>
      <rect x="340" y="846" width="150" height="6" fill="var(--ink)"/>
      <path d="M135 852 Q150 815 245 810 Q340 815 355 852" fill="none" stroke="var(--ink)" stroke-width="6"/>
      <circle cx="245" cy="978" r="64" fill="var(--seal-cream)" stroke="var(--ink)" stroke-width="5"/>
    </svg>
    <div class="neck__name">Wren</div>
    <div class="neck__seal-name">WREN</div>
    <div class="neck__region">TASMANIA</div>
  </section>

</main>
</body>
</html>
```